Edgy Fun BBQ sauce label Needed

We are looking for a new label design as we are going to start to sell our competition bbq sauce. We have had multiple 1st place wins using this sauce in NPGA BBQ competitions

The Sauce name is Drizzle Away! The sauce will be bottled in mason jars, I would like the label to play off bbq themes and "sweet heat"

The sauce will be bottled in standard mason jar 16 oz and the label size is (2.3125in” x 9.4375in ) the front logo needs to fit with in (2.3125 tall x 5in across) Since the back will have to have the food label info.

We are looking for a new label design as we are going to start to sell our competition bbq sauce. We have had multiple 1st place wins using this sauce in NPGA BBQ competitions so I would like to have award winning ribbon somewhere on the label.

We have a logo for our BBQ team this can be incorporated but it is not required. If it is incorporated to the design. it does not have to be the focal point.

We are looking for this label to stand out and grab their attention we like to have fun and push the envelope a bit so don't be timid with the design.

Sauce Description: The award winning Dust Off! BBQ team has been bringing our local flavor to the BBQ competition circuit and now we are bringing it straight to your kitchen. Slather Sweat heat on any meat.

Here are some examples of sauces that are popular in competition bbq.

http://hickoryvaultgrill.example/

https://www.tallcedargrills.example/store/bbq-sauce/amber-goat-classic-barbecue-sauce

https://www.tallcedargrills.example/store/bbq-sauce/fieldhands-tangy-250
Updates

I would like to see on the label  in a the sauce name "Drizzle Away!"  then in smaller front "Barbecue Sauce"  - Then optional in yet smaller front "A Sweet Heat Treat" or " A Sweet Heat Treat for any Meat"

With all this I understand the Dust Off logo may not fit which is ok and it does not need to be on the label.

Reason: I know a bunch of Designers had just started to work on this project so I extended the deadline..

Target Market(s)

We are going to focus on catering, farmers markets, fairs, and BBQ competitions

Industry/Entity Type

Store

Font styles to use
Other font styles liked:
• Desdemona

Colors
eb1f27
f37022
fcf9ce
fbed23
faa54b

Requirements
Must have
• The Sauce name - Drizzle Away!
smaller then name but I would like " BBQ Sauce - Treat your meat to a sweet heat"

award winning ribbon or trophy
Nice to have
• A edgy cartoon pig or cow standing over a vantor style kettle grill using a mop style brush slathering sauce on to a rack of bbq ribs

Dust Off! BBQ in matching front from our logo

```html
<!DOCTYPE html>
<html lang="en">
<head>
<meta charset="utf-8">
<title>Drizzle Away! Barbecue Sauce Label</title>
<link rel="stylesheet" href="https://fonts.googleapis.com/css2?family=Bowlby+One&family=Oswald:wght@500;600&family=Arimo:wght@400;700&display=swap">
<style>
  :root {
    --bark: #2b1b15;
    --bark-edge: #241611;
    --cream: #fcf9ce;
    --cream-deep: #f6e7b8;
    --red: #eb1f27;
    --red-deep: #c4161d;
    --orange: #f37022;
    --orange-soft: #faa54b;
    --yellow: #fbed23;
    --ink: #1a1a1a;
    --paper: #ffffff;
  }
  * { box-sizing: border-box; margin: 0; padding: 0; }
  html, body { width: 1200px; height: 365px; overflow: hidden; background: var(--bark); }
  .label {
    position: relative;
    width: 1200px; height: 365px;
    background: var(--bark);
    font-family: "Arimo", Arial, sans-serif;
    color: var(--ink);
  }
  .panel-edge {
    position: absolute; top: 0; bottom: 0; width: 2px;
    background: var(--bark-edge);
  }
  .star { position: absolute; width: 16px; height: 16px; }
  .facts {
    position: absolute; top: 117px; height: 141px;
    background: var(--paper);
    font-size: 9.5px; line-height: 1.18;
    padding: 5px 7px;
  }
  .facts-back { left: 0; width: 275px; }
  .facts-front { left: 908px; width: 259px; }
  .facts-row { display: flex; justify-content: space-between; gap: 6px; white-space: nowrap; }
  .facts-head { font-weight: 700; border-bottom: 3px solid var(--ink); padding-bottom: 1px; margin-bottom: 2px; }
  .indent { padding-left: 12px; }
  .facts-cols { display: flex; gap: 8px; height: 100%; }
  .facts-cols > div { flex: 1; }
  .facts-title { font-weight: 700; font-size: 22px; line-height: 0.98; margin-bottom: 2px; }
  .facts-rule { border-top: 1px solid var(--ink); margin: 2px 0; }
  .facts-note { font-size: 7.5px; line-height: 1.15; margin-top: 3px; }
  .emblem { position: absolute; left: 350px; top: 0; width: 500px; height: 365px; }
  .brand-name { font-family: "Bowlby One", "Arial Black", sans-serif; }
  .sub-line { font-family: "Oswald", "Arial Narrow", sans-serif; }
</style>
</head>
<body>
<main class="label">
  <span class="panel-edge" style="left:292px"></span>
  <span class="panel-edge" style="left:900px"></span>

  <svg class="star" style="left:58px;top:67px" viewBox="0 0 20 20" aria-hidden="true"><polygon fill="var(--cream)" points="10,1 12.6,7.2 19,7.6 14,11.8 15.6,18.5 10,14.8 4.4,18.5 6,11.8 1,7.6 7.4,7.2"/></svg>
  <svg class="star" style="left:905px;top:67px" viewBox="0 0 20 20" aria-hidden="true"><polygon fill="var(--cream)" points="10,1 12.6,7.2 19,7.6 14,11.8 15.6,18.5 10,14.8 4.4,18.5 6,11.8 1,7.6 7.4,7.2"/></svg>
  <svg class="star" style="left:1142px;top:67px" viewBox="0 0 20 20" aria-hidden="true"><polygon fill="var(--cream)" points="10,1 12.6,7.2 19,7.6 14,11.8 15.6,18.5 10,14.8 4.4,18.5 6,11.8 1,7.6 7.4,7.2"/></svg>

  <section class="facts facts-back">
    <div class="facts-cols">
      <div>
        <div class="facts-row facts-head"><span></span><span>% Daily Value*</span></div>
        <div class="facts-row"><span></span><span>0%</span></div>
        <div class="facts-row"><span></span><span>0%</span></div>
        <div class="facts-row"><span></span><span>&nbsp;</span></div>
        <div class="facts-row"><span></span><span>0%</span></div>
        <div class="facts-row"><span></span><span>13%</span></div>
        <div class="facts-rule"></div>
        <div class="facts-row"><span>Vitamin C 0%</span></div>
      </div>
      <div style="flex:2.2">
        <div class="facts-row facts-head"><span>Amount/Serving</span><span>% Daily Value*</span></div>
        <div class="facts-row"><span>Total Carbohydrate 15g</span><span>5%</span></div>
        <div class="facts-row indent"><span>Dietary Fiber 1g</span><span>4%</span></div>
        <div class="facts-row indent"><span>Sugars 12g</span><span></span></div>
        <div class="facts-row"><span>Protein 0g</span><span></span></div>
        <div class="facts-row"><span>&nbsp;</span></div>
        <div class="facts-rule"></div>
        <div class="facts-row"><span>Calcium 0%</span><span>Iron 0%</span></div>
      </div>
    </div>
  </section>

  <svg class="emblem" viewBox="0 0 500 365" role="group" aria-label="Drizzle Away! Barbecue Sauce emblem">
    <rect x="52" y="40" width="380" height="222" rx="38" fill="var(--cream-deep)"/>
    <rect x="66" y="54" width="352" height="194" rx="28" fill="var(--red)"/>
    <rect x="186" y="62" width="112" height="20" rx="4" fill="var(--cream-deep)" role="img" aria-label="Row of farm animal silhouettes"/>
    <rect x="36" y="94" width="412" height="74" fill="var(--orange)"/>
    <rect x="36" y="94" width="412" height="5" fill="var(--yellow)"/>
    <rect x="36" y="163" width="412" height="5" fill="var(--yellow)"/>
    <text class="brand-name" x="242" y="150" text-anchor="middle" font-size="56" fill="var(--cream)" textLength="356" lengthAdjust="spacingAndGlyphs">DRIZZLE AWAY!</text>
    <text class="sub-line" x="242" y="196" text-anchor="middle" font-size="20" font-weight="500" fill="var(--cream)" letter-spacing="2">BARBECUE SAUCE</text>
    <line x1="118" y1="189" x2="160" y2="189" stroke="var(--cream)" stroke-width="2"/>
    <line x1="324" y1="189" x2="366" y2="189" stroke="var(--cream)" stroke-width="2"/>
    <text class="sub-line" x="242" y="230" text-anchor="middle" font-size="19" font-weight="600" fill="var(--yellow)">Treat Your Meat to a Sweet Heat</text>
    <g transform="translate(436,244)">
      <circle r="50" fill="var(--orange-soft)"/>
      <circle r="42" fill="var(--red-deep)" stroke="var(--cream)" stroke-width="2.5"/>
      <text class="brand-name" x="0" y="2" text-anchor="middle" font-size="22" fill="var(--cream)">1ST</text>
      <text class="sub-line" x="0" y="22" text-anchor="middle" font-size="13" font-weight="600" fill="var(--cream)" letter-spacing="1">PLACE</text>
    </g>
  </svg>

  <section class="facts facts-front">
    <div class="facts-cols">
      <div>
        <div class="facts-title">Nutrition Facts</div>
        <div>Serving Size 2 tbsp (28g)</div>
        <div>Servings Per Container 16</div>
        <div class="facts-rule"></div>
        <div>Calories 60</div>
        <div class="indent">Calories from Fat 0</div>
        <div class="facts-rule"></div>
        <div class="facts-note">* Percent Daily Values are based on a 2,000 calorie diet.</div>
      </div>
      <div>
        <div class="facts-row facts-head"><span>Amount/Serving</span></div>
        <div>Total Fat 0g</div>
        <div class="indent">Saturated Fat 0g</div>
        <div class="indent">Trans Fat 0g</div>
        <div>Cholesterol 0mg</div>
        <div>Sodium 310mg</div>
        <div class="facts-rule"></div>
        <div>Vitamin A 0%</div>
      </div>
    </div>
  </section>
</main>
</body>
</html>
```